QV - menu design

Hi,

We require elegant menu design for upscale restaurant. Please find attached the logo and the menu items for your reference.

for inspiration, this is a good website: -
http://www.platewhisper.example/bellfoldnotes/about.php

We are very much open for Menu Size suggestions.

unfortunately the place is going under renovation, we don't have updated images to it. the closest look and feel to our place is http://varnelo.example ..

we are also open for creative options on the shape, the styles, etc. as long as it represents the fine dine feel ...

Thanks ...

Dear All,

We wouldlike to extend our apology for not being able to provide feedbacks on everysingle design. We were extremely busy and we have multiple contests opensimultaneously which makes the process even harder.

However,we would like to thank you all for the efforts you have put into designingour menu. It is very much appreciated …

We wishyou all success in your design ventures and we are quite positive that we willbe working with many of you on many projects in the soon future. 

Thanks & Regards,

TLG Team...

 

 

 

Industry/Entity Type

Restaurant

Requirements
Must have
• Please ensure that there are 'some' images in the menu ... this is very important.
Should not have
• IMPORTANT: -

1. Please DO NOT insert any currency sign to the menu
2. Please keep the prices of the menu at the end of the menu items descriptions NOT beside the menu item names. The font of the price should be similar to the menu item description and please DO NOT bold the numbers. the prices should be subtle.

Thank you ...

```html
<!DOCTYPE html>
<html lang="en">
<head>
<meta charset="utf-8">
<title>Quillvale Café – Menu</title>
<link href="https://fonts.googleapis.com/css2?family=Crimson+Text:ital,wght@0,400;0,600;0,700;1,400;1,600;1,700&family=Raleway:wght@300;400;500&display=swap" rel="stylesheet">
<style>
  :root {
    --paper: #ffffff;
    --ink: #1f1f1f;
    --gold: #a4876a;
    --heading: #6a6a6a;
    --rule: #b9b9b9;
    --sketch-light: #e4ddd2;
    --sketch-mid: #c9bba6;
  }
  * { margin: 0; padding: 0; box-sizing: border-box; }
  html, body { width: 1200px; height: 1200px; overflow: hidden; background: var(--paper); }
  .menu {
    position: relative; width: 1200px; height: 1200px; background: var(--paper);
    color: var(--ink); font-family: "Crimson Text", Georgia, serif;
  }
  .brand {
    position: absolute; left: 95px; top: 82px; display: flex; align-items: center; gap: 14px;
    font-family: "Raleway", Arial, sans-serif; font-weight: 400; color: var(--ink);
    font-size: 40px; letter-spacing: 6px; text-transform: uppercase;
  }
  .brand-mark { width: 34px; height: 34px; background: var(--gold); }
  .sandwich-art {
    position: absolute; left: 635px; top: 155px; width: 230px; height: 145px; border-radius: 14px;
    background: radial-gradient(ellipse at center, var(--sketch-mid) 0%, var(--sketch-light) 70%, var(--paper) 100%);
  }
  .mushroom-art {
    position: absolute; left: 960px; top: 1018px; width: 190px; height: 130px; border-radius: 14px;
    background: radial-gradient(ellipse at center, var(--sketch-mid) 0%, var(--sketch-light) 70%, var(--paper) 100%);
  }
  .rule-h { position: absolute; border-top: 1.5px dotted var(--rule); height: 0; }
  .rule-v { position: absolute; border-left: 1.5px dotted var(--rule); width: 0; }
  .section-title {
    position: absolute; font-family: "Raleway", Arial, sans-serif; font-weight: 300;
    color: var(--heading); font-size: 32px; letter-spacing: 1.5px; text-transform: uppercase;
    text-align: center; line-height: 1;
  }
  .column { position: absolute; text-align: center; }
  .item { margin-bottom: 14px; }
  .item-name { color: var(--gold); font-weight: 700; font-size: 20px; line-height: 1.2; }
  .item-desc { font-style: italic; font-size: 15px; line-height: 1.3; }
  .sandwich-list { position: absolute; left: 455px; top: 372px; width: 700px; text-align: center; }
  .sandwich-list p { font-style: italic; font-size: 15.5px; line-height: 1.3; margin-bottom: 10px; }
  .sandwich-list strong { font-weight: 700; }
</style>
</head>
<body>
<main class="menu">
  <div class="brand"><span class="brand-mark"></span>Quillvale Café</div>
  <div class="sandwich-art" role="img" aria-label="Sketch of a stacked club sandwich"></div>

  <div class="rule-v" style="left:425px; top:310px; height:890px;"></div>
  <div class="rule-h" style="left:425px; top:310px; width:750px;"></div>
  <h2 class="section-title" style="left:425px; top:320px; width:750px;">The Sandwiches</h2>
  <div class="rule-h" style="left:425px; top:360px; width:750px;"></div>

  <section class="sandwich-list">
    <p><strong>Grilled Vegetables Sandwich</strong> with fresh Goat cheese and chives served with<br>our Homemade spicy garlic mayo. 59</p>
    <p><strong>Butterfish burger</strong> with fresh tomato, beef bacon, grilled vegetables and béarnaise sauce.</p>
    <p><strong>Tataki Tuna sandwich</strong> with red onion slices, stewed endives and black olives and sultanas pate'. 79</p>
    <p><strong>Beef sirloin steak sandwich</strong> with grain mustard, Parmesan cheese and fresh Nashi pears. 79</p>
    <p><strong>The Traditional Club sandwich</strong> served with French fries and vegetable chips. 69</p>
    <p><strong>Chicken sandwich</strong> with Parmesan cheese slices, sundried tomatoes and mint Flavored mayo. 69</p>
  </section>

  <div class="rule-h" style="left:75px; top:367px; width:350px;"></div>
  <h2 class="section-title" style="left:75px; top:375px; width:350px;">The Breakfast</h2>
  <div class="rule-h" style="left:75px; top:410px; width:350px;"></div>

  <section class="column" style="left:78px; top:420px; width:340px;">
    <div class="item"><div class="item-name">Butter Croissant</div><div class="item-desc">Served plain with a selection of two jams, a vanilla custard cream, a chocolate cream and butter curls. 36</div></div>
    <div class="item"><div class="item-name">Cheese Croissant</div><div class="item-desc">Crumbly freshly baked with cheese filling. 29</div></div>
    <div class="item"><div class="item-name">Daily Fresh Eggs</div><div class="item-desc">A choice of (poached, scrambled, pan fried, omelet) all served with toasted bread, mushrooms, roasted tomatoes and chicken sausages. 59</div></div>
    <div class="item"><div class="item-name">Healthy Time</div><div class="item-desc">One choice of hot beverage from our<br>cafe served with fruit salad, natural Yoghurt,<br>whole wheat bread vegetable sandwiches and<br>sugar free biscuits selection.49</div></div>
    <div class="item"><div class="item-name">Energy Time</div><div class="item-desc">One choice of hot beverage from our cafe served with finger chocolate muffins, Poached egg with toasted bread and crispy beef bacon, crepe roll with goat Cheese and honey and finger chocolate cream with salted cookies. 59</div></div>
    <div class="item"><div class="item-name">Quillvale Time</div><div class="item-desc">One choice of hot beverage from our cafe served with our selection of scones, Smoked salmon and avocado sandwich, roasted sausages sandwich, grilled vegetables sandwich, selection of our best biscuits. 59</div></div>
    <div class="item"><div class="item-name">The Arabic Breakfast</div><div class="item-desc">Choice of Zattar Manakish and Cheese Manakish, served with one choice of hot beverage from our cafe and fresh orange juice. 59</div></div>
  </section>

  <div class="rule-h" style="left:425px; top:592px; width:750px;"></div>
  <h2 class="section-title" style="left:425px; top:604px; width:510px;">Salads</h2>
  <div class="rule-h" style="left:425px; top:645px; width:750px;"></div>
  <div class="rule-v" style="left:933px; top:645px; height:555px;"></div>

  <section class="column" style="left:445px; top:660px; width:480px;">
    <div class="item"><div class="item-name">Vegetarian Salad</div><div class="item-desc">Fresh green leaves, Italian cherry tomatoes, carrots, cucumber, green apple and toasted pine nuts with our special grain mustard dressing.59</div></div>
    <div class="item"><div class="item-name">Sweet Gorgonzola Cheese Salad</div><div class="item-desc">Fresh green leaves, Gorgonzola cheese, fresh pears, walnuts, garlic bread croutons, green celery with smoked honey dressing.59</div></div>
    <div class="item"><div class="item-name">Beef Sirloin Salad</div><div class="item-desc">Fresh green leaves, beef sirloin julienne, caramelized apples, Parmesan cheese, toasted almonds, sundried tomatoes and light Pesto sauce.79</div></div>
    <div class="item"><div class="item-name">Tandoori Chicken Salad</div><div class="item-desc">Fresh green leaves, Tandoori chicken breast, fresh mango, fresh goat cheese, crispy chicken skin and Jasmine rice sauce.69</div></div>
    <div class="item"><div class="item-name">Seafood Salad</div><div class="item-desc">Fresh green leaves, fresh steamed seafood, black olives, celery, garlic bread croutons, avocado and grapefruit dressing.89</div></div>
    <div class="item"><div class="item-name">Fresh Tuna Salad</div><div class="item-desc">Fresh green leaves, low temperature cooked tuna, taggiasca olives, red onions, roasted peppers, soy marinated tofu and lemon dressing.89</div></div>
  </section>

  <h2 class="section-title" style="left:933px; top:655px; width:240px;">Soup</h2>
  <div class="rule-h" style="left:933px; top:697px; width:242px;"></div>

  <section class="column" style="left:945px; top:710px; width:220px;">
    <div class="item"><div class="item-name">Bouillabaisse</div><div class="item-desc">Traditional French<br>Seafood soup, with Saffron<br>and Estragon. 119</div></div>
    <div class="item"><div class="item-name">Barley soup</div><div class="item-desc">With fresh vegetables,<br>tomato smoothie and a hint<br>of garlic oil. 49</div></div>
    <div class="item"><div class="item-name">Beef chili</div><div class="item-desc">Served with Arabic bread,<br>fresh guacamole and<br>spicy black beans. 49</div></div>
  </section>

  <div class="mushroom-art" role="img" aria-label="Sketch of a cluster of wild mushrooms"></div>
</main>
</body>
</html>
```